Spectral Geology services flyer

We are looking for some eye-catching flyer designs templates for our company spectral geology pages. We are open to any designs but prefer the theme colour to be similar to our logo colours or something goes well with the colours.
We have attached a pptx that has texts and figures we would like to put on the flyer, please combined slide 1&2 as front page and 3-5 as back page.
Requirements:
Colour theme: similar to logo colours or something that goes well with it (logo is attached)
Page: two sides A4 size
Text & front: No specific requirements
Reference/examples:
- Below website demonstrates how we use our machines for those applications
http://www.brinvaleoptics.com/applications_home.html
- Same applies to slide 11 - 25 from link below
http://www.norrikwade.com.au/public/documents/5/18/Crustal%20Survey%20of%20Ancient%20Copper%20Belts.pdf

```html
<!DOCTYPE html>
<html lang="en">
<head>
<meta charset="utf-8">
<title>Spectral Geology and Earth Imagery – Terraline Minerals</title>
<link rel="stylesheet" href="https://fonts.googleapis.com/css2?family=Open+Sans:wght@400;600;700&family=Russo+One&family=Titillium+Web:ital,wght@1,700&display=swap">
<style>
  :root {
    --page-bg: #d9d4cc;
    --paper: #ffffff;
    --ink: #262626;
    --orange: #e8862c;
    --frame: #ecd9a6;
    --rock: #2b2724;
    --sky: #4f8fe0;
    --black: #1b1b1b;
  }
  * { box-sizing: border-box; margin: 0; padding: 0; }
  html, body { width: 1200px; height: 1200px; overflow: hidden; background: var(--page-bg); }
  .flyer {
    position: absolute; left: 190px; top: 20px;
    width: 820px; height: 1160px;
    background: var(--paper);
    font-family: "Open Sans", sans-serif;
    color: var(--ink);
    overflow: hidden;
  }
  .hero {
    position: absolute; left: 0; top: 0; width: 820px; height: 451px;
    background:
      linear-gradient(120deg, var(--rock) 0%, #3a3430 38%, rgba(58,52,48,0) 60%),
      linear-gradient(180deg, #2f6fd6 0%, #7fa9e6 45%, #c9d9ee 70%, #4a4440 100%);
  }
  .hero-title {
    position: absolute; right: 46px; top: 42px; text-align: right;
    font-family: "Russo One", sans-serif; color: #fff; line-height: 1;
    letter-spacing: 1px;
  }
  .hero-title .line-1 { display: block; font-size: 44px; }
  .hero-title .line-2 { display: block; font-size: 33px; margin-top: 3px; }
  .thumbs { position: absolute; top: 335px; left: 46px; width: 728px; height: 162px; }
  .thumb {
    position: absolute; top: 0; width: 162px; height: 162px;
    border: 8px solid var(--frame);
  }
  .thumb-1 { left: 0;   background: linear-gradient(180deg, #2d5fb8 0%, #8aa9d0 45%, #b9a491 65%, #d8d1c9 100%); }
  .thumb-2 { left: 188px; background: linear-gradient(150deg, #3a4a2a 0%, #6e6a4a 40%, #b08a70 60%, #4c4a3a 100%); }
  .thumb-3 { left: 377px; background: linear-gradient(160deg, #b9bfc6 0%, #7b8088 40%, #4a4f55 70%, #c8a890 100%); }
  .thumb-4 { left: 566px; background: linear-gradient(180deg, #a9bcd6 0%, #c9d2dc 40%, #b5572e 62%, #9aa0a6 100%); }
  .column { position: absolute; top: 523px; width: 350px; font-size: 16px; line-height: 22.6px; }
  .column-left { left: 46px; }
  .column-right { left: 422px; }
  .column p { margin-bottom: 22px; }
  .accent { color: var(--orange); }
  .tagline {
    position: absolute; left: 422px; top: 920px;
    font-family: "Titillium Web", sans-serif; font-style: italic; font-weight: 700;
    font-size: 28px; line-height: 38px; color: var(--orange);
  }
  .brand {
    position: absolute; left: 50px; top: 1053px;
    display: flex; align-items: center; gap: 12px;
  }
  .brand-dot { width: 50px; height: 50px; border-radius: 50%; background: var(--orange); }
  .brand-name { font-family: "Open Sans", sans-serif; font-weight: 700; font-size: 28px; color: var(--ink); }
  .contact-band { position: absolute; left: 446px; top: 1040px; width: 374px; height: 70px; }
  .contact-text {
    position: absolute; right: 44px; top: 1046px; text-align: right; color: #fff;
  }
  .contact-phone { font-family: "Russo One", sans-serif; font-size: 24px; letter-spacing: 1px; display: block; }
  .contact-web { font-size: 17px; display: block; margin-top: 1px; }
</style>
</head>
<body>
<main class="flyer">
  <div class="hero" role="img" aria-label="Geologist in hard hat and safety vest examining a dark rock outcrop under a blue sky"></div>
  <h1 class="hero-title"><span class="line-1">SPECTRAL GEOLOGY</span><span class="line-2">AND EARTH IMAGERY</span></h1>

  <div class="thumbs">
    <div class="thumb thumb-1" role="img" aria-label="Geologist crouching on rocky mountain terrain"></div>
    <div class="thumb thumb-2" role="img" aria-label="Hand-held spectrometer scanning a soil sample"></div>
    <div class="thumb thumb-3" role="img" aria-label="Drill core sample held over core trays"></div>
    <div class="thumb thumb-4" role="img" aria-label="Field worker logging core trays on red earth"></div>
  </div>

  <section class="column column-left">
    <p>Terraline Minerals provides a complete spectral geology service.</p>
    <p class="accent">Equipment hire, licencing and logistics to Asia, Africa, Australia, Canada, Europe, Pacific Rim Nations and South America.</p>
    <p>PSM / SVX specialists to acquire and validate spectral data from soil, rock chip and downhole samples (chips and core).</p>
    <p class="accent">GIS geologists to interpret spectral signatures, develop alteration models and identify mineralisation vectors.</p>
    <p>Senior geologists that integrate spectral data with drilling, false-colour imagery (satellite data), lithology, geochemical assays (geochemistry/ assays), geochron, geophysics, radiometrics and structure to generate high-quality exploration targets.</p>
  </section>

  <section class="column column-right">
    <p class="accent">Generative consultants that integrate alteration models and mineralisation vectors with tectonic models, field mapping, mineral distribution intensity and abundance maps, grade shell models and geophysical models to produce new exploration concepts.</p>
    <p>Marketing and promotions specialists to draft high impact graphics for public release and to communicate PSM results to investors.</p>
    <p class="accent">Competent Persons and QAQC systems to report PSM results in accordance with JORC and NI43-101 standards.</p>
  </section>

  <p class="tagline">Support and insight<br>to make breakthroughs</p>

  <div class="brand">
    <span class="brand-dot"></span>
    <span class="brand-name">Terraline Minerals</span>
  </div>

  <svg class="contact-band" viewBox="0 0 374 70" aria-hidden="true">
    <polygon points="30,0 374,0 374,70 0,70" fill="var(--black)"/>
    <polygon points="54,0 374,0 374,70 24,70" fill="var(--orange)"/>
  </svg>
  <div class="contact-text">
    <span class="contact-phone">+61 7 3000 41 27</span>
    <span class="contact-web">www.terralineminerals.com</span>
  </div>
</main>
</body>
</html>
```